Nordisk Boligkontor

Company is in: Denmark - Copenhagen
It sells: Restaurants and café buildings
Companys age: 25 years
Main benefit: trust with over 25 years experience

```html
<!DOCTYPE html>
<html lang="en">
<head>
<meta charset="utf-8">
<title>Nordisk Boligkontor</title>
<link href="https://fonts.googleapis.com/css2?family=Arimo:ital,wght@0,400;0,700;1,400;1,700&family=Cinzel:wght@700&display=swap" rel="stylesheet">
<style>
:root{
  --page-top:#2b0011;
  --page-bottom:#151011;
  --wine:#870030;
  --wine-dark:#5e0020;
  --stage:#2c0010;
  --cream:#f7efdc;
  --cream-deep:#efe0b9;
  --band:#f1e5c3;
  --paper:#f5f1e6;
  --navy:#1e4470;
  --burgundy:#6b0a25;
  --nav-text:#f6e2c2;
  --ink:#1a1a1a;
  --white:#ffffff;
}
*{margin:0;padding:0;box-sizing:border-box}
html,body{width:1200px;height:1086px;overflow:hidden}
body{
  position:relative;
  font-family:"Arimo",Arial,sans-serif;
  color:var(--ink);
  background:linear-gradient(180deg,var(--page-top) 0%,#26000e 45%,var(--page-bottom) 100%);
}
.abs{position:absolute}

/* header */
.brand{left:128px;top:56px;font-family:"Cinzel",serif;font-weight:700;font-size:25px;color:var(--white);letter-spacing:.2px}
.search{left:783px;top:42px;width:244px;height:34px;background:#62001e;border:1px solid #7a1030}
.search-field{position:absolute;left:4px;top:4px;width:200px;height:25px;background:var(--white);font-style:italic;font-size:12px;color:#444;padding:5px 10px}
.search-btn{position:absolute;right:3px;top:3px;width:32px;height:27px;background:linear-gradient(#9a0a3a,#6b0022);display:flex;align-items:center;justify-content:center}
.adv-search{left:918px;top:86px;font-size:14px;color:var(--white);text-decoration:underline}

/* navigation */
.nav{left:128px;top:117px;width:940px;height:55px;display:flex;background:linear-gradient(#95003a,#7d002b);border-top:1px solid #a01a48}
.nav a{height:100%;display:flex;align-items:center;justify-content:center;color:var(--nav-text);font-weight:700;font-size:18px;text-decoration:none;border-right:1px solid #6a0024;box-shadow:inset 1px 0 0 #a5224f}
.nav a.active{background:linear-gradient(#6d0024,#5a001c)}
.nav a:last-child{border-right:none}

/* stage */
.stage{left:128px;top:172px;width:940px;height:340px;background:var(--stage)}
.slider{left:148px;top:202px;width:615px;height:285px;background:linear-gradient(100deg,#c9a474 0%,#e5cb9c 25%,#6e4a32 45%,#a4876a 60%,#574032 80%,#3a2a22 100%)}
.slider-arrow{position:absolute;top:120px;font-size:42px;line-height:1;color:#6b1a12}
.slider-arrow.prev{left:22px}
.slider-arrow.next{right:22px;color:#d8d2c8}
.pager{position:absolute;left:476px;top:250px;display:flex;gap:1px}
.pager span{width:20px;height:20px;background:#c9c6c0;font-size:13px;display:flex;align-items:center;justify-content:center;color:#222}
.pager span.current{background:#5a0e12;color:var(--white)}

.side-box{left:797px;width:246px;background:linear-gradient(180deg,var(--cream) 0%,var(--cream-deep) 100%);border:1px solid #d6c08e;padding:9px 11px}
.side-box h3{font-style:italic;font-weight:400;font-size:17px;color:var(--navy)}
.side-box h3 b{font-style:normal;font-weight:700}
.side-box p{font-size:14px;line-height:21px;margin-top:6px}
.side-box .note{font-style:italic;line-height:18px}
.question{top:202px;height:130px}
.btn{position:absolute;background:linear-gradient(#a3123f,#6a0021);color:var(--white);font-weight:700;font-size:13px;display:flex;align-items:center;justify-content:center;box-shadow:1px 1px 2px rgba(0,0,0,.4)}
.btn.form{right:9px;top:89px;width:101px;height:27px}
.newsletter{top:357px;height:130px}
.mail-frame{position:absolute;left:10px;top:84px;width:230px;height:35px;background:#d9c488;padding:5px}
.mail-field{width:185px;height:25px;background:var(--white);font-style:italic;font-size:12px;color:#444;padding:5px 11px}
.btn.go{right:3px;top:4px;width:31px;height:27px}

/* welcome */
.welcome{left:128px;top:512px;width:940px;height:180px;background:var(--band);padding:6px 33px 0 35px}
.welcome h1{font-size:25px;font-weight:700;color:var(--navy)}
.welcome p{font-size:16px;line-height:25px;margin-top:4px}

/* offers */
.offers{left:128px;top:692px;width:940px;height:320px;background:var(--paper)}
.offer{position:absolute;top:10px;width:260px}
.offer h2{font-size:25px;font-weight:700;color:var(--burgundy);height:40px}
.offer .photo{width:255px;height:130px;background:var(--white);padding:5px;box-shadow:1px 2px 3px rgba(0,0,0,.35)}
.offer .photo div{width:100%;height:100%}
.offer p{font-size:14px;line-height:21px;margin-top:11px}
.offer a{display:block;margin-top:4px;font-style:italic;font-size:14px;color:var(--navy)}
.divider{position:absolute;top:28px;width:2px;height:230px;background:linear-gradient(transparent,#e8d9b0,transparent)}

.copyright{right:133px;top:1031px;font-size:12px;color:var(--white)}
</style>
</head>
<body>
<header>
  <div class="abs brand">NORDISK BOLIGKONTOR</div>
  <div class="abs search">
    <div class="search-field">Search...</div>
    <div class="search-btn">
      <svg width="18" height="18" viewBox="0 0 18 18"><circle cx="10.5" cy="7.5" r="5" fill="none" stroke="#d7c9cf" stroke-width="1.6"/><line x1="7" y1="11" x2="2" y2="16" stroke="#d7c9cf" stroke-width="2"/></svg>
    </div>
  </div>
  <a class="abs adv-search">Advanced search</a>
</header>

<nav class="abs nav">
  <a class="active" style="width:110px">Home</a>
  <a style="width:145px">For Sale</a>
  <a style="width:215px">Links/Download</a>
  <a style="width:160px">Newsletter</a>
  <a style="width:155px">About Us</a>
  <a style="width:155px">Contact Us</a>
</nav>

<section class="abs stage"></section>
<div class="abs slider" role="img" aria-label="Warm-lit restaurant interior with columns, curtains and an open kitchen">
  <span class="slider-arrow prev">&#10094;</span>
  <span class="slider-arrow next">&#10095;</span>
  <div class="pager"><span class="current">1</span><span>2</span><span>3</span><span>4</span><span>5</span><span>6</span></div>
</div>

<aside class="abs side-box question">
  <h3>Have a question?</h3>
  <p>Lorem ipsum dolor sit amet, con-<br>sectetuer adipiscing elit.</p>
  <span class="btn form">Go to form</span>
</aside>

<aside class="abs side-box newsletter">
  <h3>Get our <b>NEWSLETTER</b></h3>
  <p class="note">Enter your &nbsp;email address if you want to receive our newsletter</p>
  <div class="mail-frame"><div class="mail-field">e-mail</div><span class="btn go">Go</span></div>
</aside>

<section class="abs welcome">
  <h1>Welcome to NORDISK BOLIGKONTOR</h1>
  <p>Lorem ipsum dolor sit amet, consectetuer adipiscing elit. Aenean commodo ligula eget dolor. Aenean massa. Cum sociis natoque penatibus et magnis dis parturient montes, nascetur ridiculus mus. Donec quam felis, ultricies nec, pellentesque eu, pretium quis, sem. Nulla consequat massa quis enim. Donec pede justo, fringilla vel, aliquet nec, vulputate eget, arcu. In enim justo, rhoncus ut, imperdiet a, venenatis vitae, justo. Nullam dictum felis eu pede mollis pretium. Integer tincidunt. Cras dapibus. Vivamus elementum semper nisi.</p>
</section>

<section class="abs offers">
  <article class="offer" style="left:35px">
    <h2>Restaurant</h2>
    <div class="photo"><div role="img" aria-label="Long restaurant dining room with purple-lit tree decor" style="background:linear-gradient(180deg,#9a7ac4 0%,#6d4b8e 45%,#a88a5e 75%,#3a2a20 100%)"></div></div>
    <p>Lorem ipsum dolor sit amet, con-<br>sectetuer adipiscing elit. Aenean com-<br>modo ligula eget dolor.</p>
    <a>Read more...</a>
  </article>
  <div class="divider" style="left:315px"></div>
  <article class="offer" style="left:345px">
    <h2>Cafe</h2>
    <div class="photo"><div role="img" aria-label="Café table set with glasses and a teapot against a golden wall" style="background:linear-gradient(135deg,#c49a3a 0%,#d6b25a 45%,#a2682e 80%,#6e3a1c 100%)"></div></div>
    <p>Lorem ipsum dolor sit amet, con-<br>sectetuer adipiscing elit. Aenean com-<br>modo ligula eget dolor.</p>
    <a>Read more...</a>
  </article>
  <div class="divider" style="left:625px"></div>
  <article class="offer" style="left:655px">
    <h2>Pab</h2>
    <div class="photo"><div role="img" aria-label="Brick corner pub building with white windows" style="background:linear-gradient(180deg,#d8dce0 0%,#8a5a44 30%,#6e4030 65%,#2a2624 100%)"></div></div>
    <p>Lorem ipsum dolor sit amet, con-<br>sectetuer adipiscing elit. Aenean com-<br>modo ligula eget dolor.</p>
    <a>Read more...</a>
  </article>
</section>

<footer class="abs copyright">Copyright © 2011 NORDISK BOLIGKONTOR All rights reserved</footer>
</body>
</html>
```